Fruit and Beverage importer and distributor. F&B industry. catering mainly to touristy venues/outlet

We need a stationary design for our company in Singapore called LuvaPalm. We are a major importer and distributor of fresh thailand coconuts in Singapore hence the company name. but moving forward we intend to diversify into more fruits, juices, and beverage products to sell to our existing base of customers.
mainly catering to F&B outlets at hot tourist spots such as restaurants and theme parks and hotel chains. we core product is the fresh thai coconut. on the side we are distributing a couple of read to drink beverages
we would like to see designs that are fun and refreshing. think tropical holiday theme.
ive attached our company logo and a photo of a general look and feel id like to see for our stationary.

```html
<!DOCTYPE html>
<html lang="en">
<head>
<meta charset="utf-8">
<title>LuvaPalm Letterhead</title>
<link rel="stylesheet" href="https://fonts.googleapis.com/css2?family=Questrial&family=Montserrat:wght@700;800&display=swap">
<style>
  :root {
    --backdrop: #ececec;
    --paper: #ffffff;
    --ink: #3a3a3a;
    --ink-soft: #5c5c5c;
    --ink-faint: #9a9a9a;
    --strip: #cdcdcd;
    --brand-red: #d8262e;
    --fruit-yellow: #f5c531;
    --fruit-orange: #f08a2c;
    --fruit-red: #e2473b;
    --fruit-green: #9cc543;
  }
  * { box-sizing: border-box; margin: 0; padding: 0; }
  html, body { width: 1200px; height: 968px; overflow: hidden; }
  body {
    background: var(--backdrop);
    font-family: "Questrial", sans-serif;
    color: var(--ink-soft);
    position: relative;
  }
  .letterhead {
    position: absolute;
    left: 282px; top: 34px;
    width: 636px; height: 900px;
    background: var(--paper);
    box-shadow: 0 0 0 1px rgba(0,0,0,0.06), 0 8px 22px rgba(0,0,0,0.16);
    overflow: hidden;
  }
  .header-band { position: absolute; left: 0; top: 0; width: 636px; height: 120px; }
  .brand {
    position: absolute; left: 452px; top: 62px;
    display: flex; align-items: center; gap: 8px;
    font-family: "Montserrat", sans-serif;
    font-weight: 800; font-size: 22px;
    color: var(--brand-red);
    letter-spacing: 0.5px;
  }
  .brand-dot { width: 14px; height: 14px; border-radius: 50%; background: var(--fruit-green); }
  .letter-body { position: absolute; left: 60px; top: 138px; width: 516px; }
  .salutation {
    font-family: "Montserrat", sans-serif; font-weight: 700;
    font-size: 12.5px; color: var(--ink); margin-bottom: 12px;
  }
  .letter-body p {
    font-size: 10.5px; line-height: 1.55; margin-bottom: 13px;
    text-align: justify;
  }
  .sign-off { position: absolute; right: 60px; top: 628px; width: 220px; text-align: right; }
  .signature {
    display: block; width: 170px; height: 46px; margin: 0 0 8px auto;
    background: linear-gradient(90deg, rgba(111,127,196,0.05), rgba(111,127,196,0.3), rgba(111,127,196,0.05));
    border-radius: 4px;
  }
  .closing { font-size: 10.5px; color: var(--ink-soft); }
  .signatory {
    font-family: "Montserrat", sans-serif; font-weight: 700;
    font-size: 13px; color: var(--ink); margin-top: 10px;
  }
  .page-footer {
    position: absolute; left: 0; right: 0; bottom: 0; height: 162px;
    display: flex; flex-direction: column;
  }
  .contact-line {
    height: 30px; padding: 0 28px;
    display: flex; justify-content: space-between; align-items: center;
    font-size: 9.5px; color: var(--ink-soft);
  }
  .contact-phone { display: flex; align-items: center; gap: 5px; }
  .contact-phone svg { width: 10px; height: 10px; }
  .contact-web strong { color: var(--brand-red); font-weight: 400; }
  .contact-reg { color: var(--ink-faint); font-size: 8px; }
  .footer-strip { height: 12px; background: var(--strip); }
  .footer-band {
    flex: 1;
    background: linear-gradient(100deg, var(--fruit-yellow) 0%, var(--fruit-red) 22%, var(--fruit-orange) 40%, var(--fruit-green) 58%, var(--fruit-yellow) 76%, var(--fruit-red) 100%);
    opacity: 0.9;
  }
</style>
</head>
<body>
  <main class="letterhead">
    <svg class="header-band" viewBox="0 0 636 120" role="img" aria-label="Colourful pattern of tropical fruits: watermelon, pineapple, pear, orange and berries">
      <defs>
        <linearGradient id="fruitTones" x1="0" y1="0" x2="1" y2="0.2">
          <stop offset="0" stop-color="#f5c531"/>
          <stop offset="0.22" stop-color="#e2473b"/>
          <stop offset="0.42" stop-color="#f08a2c"/>
          <stop offset="0.6" stop-color="#9cc543"/>
          <stop offset="0.8" stop-color="#f5c531"/>
          <stop offset="1" stop-color="#e2473b"/>
        </linearGradient>
      </defs>
      <path d="M0 10 H636 V74 H586 C560 74 556 40 530 40 H470 C444 40 440 74 414 74 H0 Z" fill="#cdcdcd"/>
      <path d="M0 0 H636 V62 H586 C560 62 556 28 530 28 H470 C444 28 440 62 414 62 H0 Z" fill="url(#fruitTones)" opacity="0.9"/>
    </svg>

    <div class="brand"><span class="brand-dot"></span>LuvaPalm</div>

    <section class="letter-body">
      <h1 class="salutation">Dear sir / madame,</h1>
      <p>Lorem ipsum dolor sit amet, consectetur adipisicing elit, sed do eiusmod tempor incididunt ut labore et dolore magna aliqua. Ut enim ad minim veniam, quis nostrud exercitation ullamco laboris nisi ut aliquip ex ea commodo consequat. Duis aute irure dolor in reprehenderit in voluptate velit esse cillum dolore eu fugiat nulla pariatur. Excepteur sint occaecat cupidatat non proident, sunt in culpa qui officia deserunt mollit anim id est laborum. Lorem ipsum dolor sit amet, consectetur adipisicing elit, sed do eiusmod tempor incididunt ut labore et dolore magna aliqua. Ut enim ad minim veniam, quis nostrud exercitation ullamco laboris nisi ut aliquip ex ea commodo consequat. Duis aute irure dolor in reprehenderit in voluptate velit esse cillum dolore eu fugiat nulla pariatur. Excepteur sint occaecat cupidatat non proident, sunt in culpa qui officia deserunt mollit anim id est laborum.</p>
      <p>Lorem ipsum dolor sit amet, consectetur adipisicing elit, sed do eiusmod tempor incididunt ut labore et dolore magna aliqua. Ut enim ad minim veniam, quis nostrud exercitation ullamco laboris nisi ut aliquip ex ea commodo consequat. Duis aute irure dolor in reprehenderit in voluptate velit esse cillum dolore eu fugiat nulla pariatur. Excepteur sint occaecat cupidatat non proident, sunt in culpa qui officia deserunt mollit anim id est laborum.</p>
      <p>Lorem ipsum dolor sit amet, consectetur adipisicing elit, sed do eiusmod tempor incididunt ut labore et dolore magna aliqua. Ut enim ad minim veniam, quis nostrud exercitation ullamco laboris nisi ut aliquip ex ea commodo consequat. Duis aute irure dolor in reprehenderit in voluptate velit esse cillum dolore eu fugiat nulla pariatur. Excepteur sint occaecat cupidatat non proident, sunt in culpa qui officia deserunt mollit anim id est laborum.</p>
      <p>Lorem ipsum dolor sit amet, consectetur adipisicing elit, sed do eiusmod tempor incididunt ut labore et dolore magna aliqua. Ut enim ad minim veniam, quis nostrud exercitation ullamco laboris nisi ut aliquip ex ea commodo consequat. Duis aute irure dolor in reprehenderit in voluptate velit esse cillum dolore eu fugiat nulla pariatur. Excepteur sint occaecat cupidatat non proident, sunt in culpa qui officia deserunt mollit anim id est laborum.</p>
    </section>

    <section class="sign-off">
      <span class="signature" role="img" aria-label="Handwritten signature of Dara Kemsin"></span>
      <p class="closing">Yours Sincerely,</p>
      <p class="signatory">Dara Kemsin</p>
    </section>

    <footer class="page-footer">
      <div class="contact-line">
        <span class="contact-address">48 Harbour Lane, #07-03 Palmview Tower, Singapore 058321</span>
        <span class="contact-phone">
          <svg viewBox="0 0 10 10" aria-hidden="true"><path d="M2 1 L4 1 L4.6 3 L3.5 3.8 C4 5 5 6 6.2 6.5 L7 5.4 L9 6 L9 8 C9 8.6 8.6 9 8 9 C4.5 8.8 1.2 5.5 1 2 C1 1.4 1.4 1 2 1 Z" fill="#d8262e"/></svg>
          +65 641 27508
        </span>
        <span class="contact-web">www.<strong>luvapalm</strong>.com.sg</span>
        <span class="contact-reg">Reg. No. 201847316</span>
      </div>
      <div class="footer-strip"></div>
      <div class="footer-band" role="img" aria-label="Colourful pattern of tropical fruits: pear, pineapple, watermelon, tomato, banana and berries"></div>
    </footer>
  </main>
</body>
</html>
```